BUSINESS CARD needed for TRAVEL BUSINESS

-Background-

Wandorvist Crew (WC) is a newly found company in Asia that trains and develops people with various demographics to become a FREQUENT TRAVELER & an ENTREPRENEUR combined. Basically, the core product that the company markets teaches people how to TRAVEL leisurely and yet EARN MONEY at the same time. Our main quote will be ROAM WIDE, EARN DAILY.

- The Job -

We will be constantly going out to different events, whether opening promotional booths in roadshows or at colleges or going for networking events. Thus we need a BUSINESS CARD design that portrays our POSITIONING & BRANDING

- Positioning -

TRAVEL LEISURELY & EARN at the SAME TIME

- Objective -

Serve as a BTL marketing & networking tool

- Target Audience -

Male & Females aged 19 - 35 who LOVES to TRAVEL & have strong aspirations to make it big and attaining financial freedom. The audience are enthusiastic and when they see an opportunity, they will seize it on the very spot. They are well connected and have a wide social network.

- Single Minded Proposition -

WC is My Dream Life

Target Market(s)

REFER TO CREATIVE BRIEF

Industry/Entity Type

Marketing

Requirements
Must have
• 1) The business card must portray a branding thats related to TRAVEL.

Boarding pass design was what we came up with but express your creativity and surprise me with better ideas. :)
Nice to have
• This is an idea that we have and we would most likely like to use however I do not want to restrict your creativity so i am putting in NICE TO HAVE instead.

Our idea design -> To have the namecard in the format of a BOARDING PASS lookalike

(You may refer to these weblink for inspiration -> https://www.pictofind.example/search?hl=en&q=boarding+pass&bav=on.2,or.r_gc.r_pw.r_cp.r_qf.,cf.osb&biw=1366&bih=667&um=1&ie=UTF-8&tbm=isch&source=og&sa=N&tab=wi&ei=l-f9T4KqC4fWrQfx8eC-Bg

or simply PICTOFIND BOARDING PASS IMAGES

```html
<!DOCTYPE html>
<html lang="en">
<head>
<meta charset="utf-8">
<title>Wandorvist Crew — Business Card</title>
<link href="https://fonts.googleapis.com/css2?family=Archivo:wght@400;800&family=Roboto+Slab:wght@400&family=Oswald:wght@700&display=swap" rel="stylesheet">
<style>
  :root {
    --stage: #8c8c8b;
    --paper: #f1f1ef;
    --paper-shade: #dedede;
    --brand-blue: #233c96;
    --ink: #1d1d1d;
    --muted: #6f6f6f;
    --stripe: #0d0d0d;
  }
  * { box-sizing: border-box; margin: 0; padding: 0; }
  html, body {
    width: 1200px; height: 792px; overflow: hidden;
    background: var(--stage);
  }
  .canvas { position: relative; width: 1200px; height: 792px; }

  .card {
    position: absolute;
    background: radial-gradient(ellipse at 30% 30%, var(--paper) 0%, var(--paper) 55%, var(--paper-shade) 100%);
    box-shadow: 0 6px 18px rgba(0,0,0,.28);
    overflow: hidden;
  }

  /* Front */
  .card-front { left: 70px; top: 236px; width: 560px; height: 320px; }
  .front-brand {
    position: absolute; left: 40px; right: 40px; top: 108px;
    text-align: right;
  }
  .brand-name {
    font-family: "Archivo", Arial, sans-serif;
    font-weight: 800; font-size: 50px; letter-spacing: -1px;
    color: var(--brand-blue); line-height: 1;
  }
  .front-tagline {
    font-family: "Archivo", Arial, sans-serif;
    font-weight: 400; font-size: 15px; letter-spacing: 3px;
    color: var(--ink); margin-top: 10px;
  }
  .front-url {
    position: absolute; left: 0; right: 0; bottom: 26px; text-align: center;
    font-family: "Archivo", Arial, sans-serif; font-size: 11px; letter-spacing: 3px;
    color: var(--muted);
  }

  /* Back */
  .card-back { left: 790px; top: 116px; width: 320px; height: 560px; }
  .mag-stripe {
    position: absolute; left: 24px; top: 0; bottom: 0; width: 44px;
    background: var(--stripe);
  }
  .back-content { position: absolute; left: 90px; right: 22px; top: 26px; }
  .back-brand {
    font-family: "Archivo", Arial, sans-serif; font-weight: 800;
    font-size: 24px; color: var(--brand-blue); letter-spacing: -.5px;
    margin-bottom: 14px;
  }
  .field {
    position: relative; padding: 8px 0 6px;
    border-bottom: 1.5px solid var(--brand-blue);
  }
  .field::after {
    content: ""; position: absolute; right: 0; bottom: 0;
    width: 1.5px; height: 56px; background: var(--brand-blue);
  }
  .field::before {
    content: ""; position: absolute; right: 0; top: -1px;
    width: 6px; height: 1.5px; background: var(--brand-blue);
  }
  .field-label {
    font-family: "Archivo", Arial, sans-serif; font-size: 8px; letter-spacing: .8px;
    color: var(--muted); text-transform: uppercase;
  }
  .field-value {
    font-family: "Roboto Slab", Georgia, serif; font-size: 15px;
    color: var(--ink); margin-top: 4px; white-space: nowrap;
  }
  .field + .field { margin-top: 12px; }

  .notice {
    position: absolute; left: 90px; right: 22px; bottom: 24px; height: 140px;
  }
  .notice svg { position: absolute; inset: 0; }
  .notice-text {
    position: absolute; left: 0; bottom: 0;
    font-family: "Oswald", Impact, sans-serif; font-weight: 700;
    font-size: 13px; color: var(--ink); letter-spacing: .3px;
  }
</style>
</head>
<body>
<main class="canvas">

  <section class="card card-front" aria-label="Card front">
    <div class="front-brand">
      <div class="brand-name">Wandorvist Crew</div>
      <div class="front-tagline">ROAM WIDE, EARN DAILY</div>
    </div>
    <div class="front-url">www.wandorvist.example</div>
  </section>

  <section class="card card-back" aria-label="Card back, boarding pass style">
    <div class="mag-stripe"></div>
    <div class="back-content">
      <div class="back-brand">Wandorvist Crew</div>
      <div class="field">
        <div class="field-label">Name</div>
        <div class="field-value">MAREN ODUYA</div>
      </div>
      <div class="field">
        <div class="field-label">Phone</div>
        <div class="field-value">(+00) 555 018 274</div>
      </div>
      <div class="field">
        <div class="field-label">E-mail</div>
        <div class="field-value">office@wandorvist.example</div>
      </div>
      <div class="field">
        <div class="field-label">Website</div>
        <div class="field-value">www.wandorvist.example</div>
      </div>
      <div class="field">
        <div class="field-label">Social</div>
        <div class="field-value">social.example/wandorvist</div>
      </div>
    </div>
    <div class="notice">
      <svg viewBox="0 0 208 140" preserveAspectRatio="none">
        <polygon points="208,0 208,118 40,118" fill="var(--brand-blue)"/>
      </svg>
      <div class="notice-text">DO NOT BEND THIS CARD.</div>
    </div>
  </section>

</main>
</body>
</html>
```